Page Layouts for Australian Political Party

The Forward Signal Party of Australia has a design for its logo and now is looking for a website proposal. The initial website is being powered by blogger with plans to move to an ExpressionEngine based site. The current website is at www.fspartyhub.org

Its likely if we see a design within the next 2 days we like it will be selected before the 5 days has expired.

Target Market(s)

Looking for a design that will appeal to both the "online" generation as well as more casual internet users. These users might be comfortable with online banking and perhaps mailnest/talkloop but not much more.

I personally like the "feel" of vimrol.com and plumtreelabs.com. You might like to look at the other major political parties in Australia to see what probably quite a lot of "market testing" and money is acceptable to the Australian population. We are aiming for Generation X and younger and well as the baby boomers who get the 2.0 internet.

Industry/Entity Type

Political

Requirements
Must have
• The ability to scale elegantly across a full ExpressionEngine implementation, forums, blogs, homepage etc.
• Also look elegant on the initial blogger driven page.
• Navigation that could contain all the items on the www.unityfront.org.au site, you can use these as the place holder names for the navigation design. The short name for the party is FSP. The
Nice to have
• feel distinct from the other major parties websites. we do have views more in line with the orchardists/reformists in this country.
Should not have
• basic stuff, not look like a pagenook page ;) imagery too similar from any of the other parties...

```html
<!DOCTYPE html>
<html lang="en">
<head>
<meta charset="utf-8">
<title>Forward Signal Party of Australia – Page Layouts</title>
<link rel="stylesheet" href="https://fonts.googleapis.com/css2?family=Source+Sans+3:wght@400;600;700&display=swap">
<style>
:root{
  --page:#ffffff;
  --panel-top:#e6e7e9;
  --panel-bottom:#b9bbbe;
  --navy:#17207a;
  --navy-deep:#0c0f5a;
  --royal:#1d3fa8;
  --sky:#10a6e6;
  --sky-light:#3cc0f2;
  --orange:#f07d1e;
  --orange-light:#f7b33a;
  --green:#7fae2a;
  --green-light:#a9c93b;
  --ink:#1b1b1b;
  --body-ink:#333333;
  --link:#3a4cb0;
  --white:#ffffff;
  --font:"Source Sans 3", "Myriad Pro", Arial, sans-serif;
}
*{box-sizing:border-box;margin:0;padding:0}
html,body{width:829px;height:1200px;overflow:hidden;background:var(--page);font-family:var(--font);color:var(--ink)}
.canvas{position:relative;width:829px;height:1200px}
.layout{position:absolute;left:23px;width:763px;background:linear-gradient(180deg,var(--panel-top) 0%,var(--panel-top) 40%,var(--panel-bottom) 100%)}
.layout--home{top:35px;height:576px}
.layout--blog{top:650px;height:474px}

/* brand */
.brand{position:absolute;left:60px;top:17px;display:flex;flex-direction:column;align-items:center;gap:6px}
.brand__mark{width:40px;height:40px;border-radius:6px;background:var(--royal)}
.brand__name{font-size:15px;font-weight:600;color:var(--navy-deep);letter-spacing:-.2px;white-space:nowrap}

/* banner */
.banner{position:absolute;left:55px;top:90px;width:653px;height:181px;border-radius:10px;overflow:hidden;background:linear-gradient(100deg,var(--navy-deep) 0%,var(--royal) 55%,#2a5cc4 100%)}
.photo{position:absolute;background:linear-gradient(160deg,#c9a98d 0%,#6b84b4 55%,#2c3f86 100%)}
.photo--crowd{left:392px;top:38px;width:316px;height:206px;border-radius:0 10px 0 0}

/* nav */
.nav{position:absolute;left:55px;width:653px;height:27px;background:linear-gradient(180deg,var(--sky-light),var(--sky));display:flex;align-items:center;justify-content:space-between;padding:0 8px;border-radius:0 0 10px 10px}
.nav a{color:var(--white);font-size:8.6px;text-decoration:none;letter-spacing:.1px;white-space:nowrap;padding:0 5px;line-height:17px;border-left:1px solid rgba(255,255,255,.7)}
.nav a:first-child{border-left:0;padding-left:0}
.layout--home .nav{top:244px}
.layout--blog .nav{top:104px;border-radius:0 0 8px 8px}

/* features strip */
.features{position:absolute;left:55px;top:283px;width:653px;height:87px;border-radius:9px;background:linear-gradient(180deg,#d6d7d9,#a9abae);display:flex}
.features > div{position:relative;border-left:1px solid #f2f2f2}
.features > div:first-child{border-left:0}
.hot{width:164px;display:flex;flex-direction:column;justify-content:center;align-items:center;line-height:.85}
.hot span{font-weight:700;letter-spacing:-1px;color:var(--sky)}
.hot .hot__a{font-size:44px}
.hot .hot__b{font-size:31px;color:var(--royal);font-weight:600}
.video{width:173px}
.video__frame{position:absolute;left:12px;top:6px;width:136px;height:72px;border:1px solid var(--royal);background:linear-gradient(90deg,#7b8fa8,#c7cfda 50%,#e2d6c8)}
.video__play{position:absolute;left:67px;top:46px;width:24px;height:24px;border-radius:50%;background:#1b2c55;border:2px solid #fff}
.video__play::after{content:"";position:absolute;left:8px;top:5px;border-left:8px solid var(--sky);border-top:5px solid transparent;border-bottom:5px solid transparent}
.tool{width:163px}
.newsletter{width:153px}
.card{position:absolute;left:13px;top:7px;width:134px;height:70px;background:#f4f4f5}
.card__head{background:var(--navy);color:var(--white);font-size:9.8px;font-weight:600;padding:4px 7px;height:21px}
.tool .card__label{font-size:8.6px;color:var(--link);padding:4px 7px 0;line-height:1.15}
.tool .card__input{position:absolute;left:7px;top:50px;width:75px;height:11px;background:#fff}
.tool .card__search{position:absolute;right:8px;top:27px;width:40px;height:40px;border-radius:50%;background:radial-gradient(circle at 40% 35%,#fff,#b7b9bd)}
.tool .card__search svg{position:absolute;left:8px;top:7px}
.newsletter .card{left:17px}
.newsletter .card__input{margin:6px 7px 0;background:#fff;height:12px;font-size:8.4px;color:var(--link);padding:0 3px;line-height:12px}
.newsletter .card__btn{display:inline-block;margin:6px 7px 0;background:var(--navy);color:#fff;font-size:8.6px;font-weight:600;padding:2px 4px}

/* columns */
.col{position:absolute;background:var(--white);overflow:hidden}
.col__head{height:31px;color:var(--white);font-size:18px;font-weight:600;padding:4px 12px;letter-spacing:.2px}
.col--news .col__head{background:linear-gradient(180deg,var(--orange),var(--orange-light))}
.col--blog .col__head{background:linear-gradient(180deg,var(--navy-deep),var(--royal))}
.col--ideas .col__head{background:linear-gradient(180deg,var(--green),var(--green-light))}
.story{padding:6px 11px 5px;border-bottom:1px dashed #888}
.story:last-child{border-bottom:0}
.story h3,.post h3{font-size:9.8px;font-weight:600;color:var(--ink);line-height:1.2}
.story p,.post p{font-size:7.5px;line-height:1.28;color:var(--body-ink);margin-top:1px}
.post{padding:7px 11px}
.post p + p{margin-top:8px}
.layout--home .col{top:380px;height:177px}
.col--news{left:55px;width:164px}
.col--blog{left:232px;width:300px}
.col--ideas{left:545px;width:163px}
.photo--megaphone{position:relative;width:100%;height:85px;background:linear-gradient(90deg,#4a3a30 0%,#6fa7d8 45%,#9cd2f3 100%)}
.layout--blog .col{top:154px;height:290px}
.layout--blog .col--blog{width:476px}
.layout--blog .post h3{font-size:13px;margin-bottom:4px}
.layout--blog .post{width:275px;padding-top:8px}
.photo--team{left:296px;top:44px;width:166px;height:138px;background:linear-gradient(120deg,#d9dde2 0%,#5b5a62 55%,#1d1d22 100%)}

.dark-band{position:absolute;left:55px;top:90px;width:653px;height:14px;background:var(--navy)}
.photo--bench{left:515px;top:7px;width:165px;height:84px;background:linear-gradient(180deg,#c6a78f 0%,#b6764a 60%,#7a4a28 100%)}
</style>
</head>
<body>
<div class="canvas">

  <section class="layout layout--home">
    <div class="banner"></div>
    <div class="photo photo--crowd" role="img" aria-label="Photo of a smiling group of young supporters sitting together"></div>
    <div class="brand">
      <div class="brand__mark"></div>
      <div class="brand__name">Forward Signal</div>
    </div>
    <nav class="nav">
      <a>ECONOMY</a><a>SMALL BUSINESS</a><a>COMMUNITY</a><a>SENIORS</a><a>NATIONAL SECURITY</a><a>HEALTH</a><a>EDUCATION</a><a>ENVIRONMENT</a><a>REGIONAL</a><a>INFRASTRUCTURE</a>
    </nav>

    <div class="features">
      <div class="hot"><span class="hot__a">HOT</span><span class="hot__b">TOPICS</span></div>
      <div class="video">
        <div class="video__frame" role="img" aria-label="Video still of a candidate speaking in an office"></div>
        <div class="video__play"></div>
      </div>
      <div class="tool">
        <div class="card">
          <div class="card__head">FIND YOUR ELECTORATE</div>
          <div class="card__label">Postcode, suburb<br>or electorate</div>
          <div class="card__input"></div>
          <div class="card__search">
            <svg width="24" height="26" viewBox="0 0 24 26" aria-hidden="true"><circle cx="9" cy="9" r="6.5" fill="#d9ecff" stroke="#555" stroke-width="2"/><path d="M13.5 14 L21 23" stroke="#2a2f8a" stroke-width="4" stroke-linecap="round"/></svg>
          </div>
        </div>
      </div>
      <div class="newsletter">
        <div class="card">
          <div class="card__head">NEWSLETTER SIGN UP</div>
          <div class="card__input">Email</div>
          <span class="card__btn">SUBMIT</span>
        </div>
      </div>
    </div>

    <div class="col col--news">
      <div class="col__head">LATEST NEWS</div>
      <article class="story"><h3>Lorem Ipsum Dolor Sit Amet</h3><p>Consectetur adipiscing elit. Maecenas interdum tincidunt sem, non congue dui luctus euismod. Phasellus fringilla imperdiet auctor. Morbi massa nibh, accumsan a tempus ut, commodo vitae. &gt;</p></article>
      <article class="story"><h3>Lorem Ipsum Dolor Sit Amet</h3><p>Consectetur adipiscing elit. Maecenas interdum tincidunt sem, non congue dui luctus euismod. Phasellus fringilla imperdiet auctor. Morbi massa nibh, accumsan a tempus ut, commodo vitae. &gt;</p></article>
    </div>
    <div class="col col--blog">
      <div class="col__head">BLOG</div>
      <article class="post"><h3>Lorem Ipsum Dolor Sit Amet</h3>
        <p>Consectetur adipiscing elit. Maecenas interdum tincidunt sem, non congue dui luctus euismod. Phasellus fringilla imperdiet auctor. Morbi massa nibh, accumsan a tempus ut, commodo vitae.</p>
        <p>Nam placerat augue sodales diam luctus eget tristique augue semper. Aenean id elit ac sem iaculis venenatis in ut magna. Suspendisse ut eros ante, vel adipiscing lectus. Pellentesque quis dolor justo. Pellentesque in leo felis. Fusce fermentum auctor risus, sit amet fermentum felis cursus in. Morbi condimentum mi vehicula nunc aliquet pellentesque. Nullam congue placerat diam, at bibendum felis tristique at. Vestibulum egestas, purus vitae mattis placerat, velit nulla facilisis neque, ac pellentesque enim ligula ut ipsum. Nulla vel sagittis metus. Mauris vulputate, enim eget fringilla laoreet, velit lorem cursus ipsum, at elementum quam purus et lorem.</p>
      </article>
    </div>
    <div class="col col--ideas">
      <div class="col__head">YOUR IDEAS</div>
      <div class="photo--megaphone" role="img" aria-label="Illustration of a man shouting through a megaphone against a blue sky"></div>
      <article class="post"><h3>Lorem Ipsum Dolor Sit Amet</h3><p>Consectetur adipiscing elit. Maecenas interdum tincidunt sem, non congue dui luctus euismod. Phasellus fringilla &gt;</p></article>
    </div>
  </section>

  <section class="layout layout--blog">
    <div class="photo photo--bench" role="img" aria-label="Photo of young people sitting on a park bench, seen from behind"></div>
    <div class="brand">
      <div class="brand__mark"></div>
      <div class="brand__name">Forward Signal</div>
    </div>
    <div class="dark-band"></div>
    <nav class="nav">
      <a>ECONOMY</a><a>SMALL BUSINESS</a><a>COMMUNITY</a><a>SENIORS</a><a>NATIONAL SECURITY</a><a>HEALTH</a><a>EDUCATION</a><a>ENVIRONMENT</a><a>REGIONAL</a><a>INFRASTRUCTURE</a>
    </nav>

    <div class="col col--news">
      <div class="col__head">LATEST NEWS</div>
      <article class="story"><h3>Lorem Ipsum Dolor Sit Amet</h3><p>Consectetur adipiscing elit. Maecenas interdum tincidunt sem, non congue dui luctus euismod. Phasellus fringilla imperdiet auctor. Morbi massa nibh, accumsan a tempus ut, commodo vitae. &gt;</p></article>
      <article class="story"><h3>Lorem Ipsum Dolor Sit Amet</h3><p>Consectetur adipiscing elit. Maecenas interdum tincidunt sem, non congue dui luctus euismod. Phasellus fringilla imperdiet auctor. Morbi massa nibh, accumsan a tempus ut, commodo vitae. &gt;</p></article>
      <article class="story"><h3>Lorem Ipsum Dolor Sit Amet</h3><p>Consectetur adipiscing elit. Maecenas interdum tincidunt sem, non congue dui luctus euismod. Phasellus fringilla imperdiet auctor. Morbi massa nibh, accumsan a tempus ut, commodo vitae. bibendum ultrices, sem est consectetur elit, ut hendrerit sapien augue nec quam. Nunc felis orci, placerat vitae ornare ut, pellentesque nec nisi.&gt;</p></article>
    </div>
    <div class="col col--blog">
      <div class="col__head">BLOG</div>
      <article class="post"><h3>Lorem Ipsum Dolor Sit Amet</h3>
        <p>Consectetur adipiscing elit. Maecenas interdum tincidunt sem, non congue dui luctus euismod. Phasellus fringilla imperdiet auctor. Morbi massa nibh, accumsan a tempus ut, commodo vitae.</p>
        <p>Nam placerat augue sodales diam luctus eget tristique augue semper. Aenean id elit ac sem iaculis venenatis in ut magna. Suspendisse ut eros ante, vel adipiscing lectus. Pellentesque quis dolor justo. Pellentesque in leo felis. Fusce fermentum auctor risus, sit amet fermentum felis cursus in. Morbi condimentum mi vehicula nunc aliquet pellentesque. Nullam congue placerat diam, at bibendum felis tristique at. Vestibulum egestas, purus vitae mattis placerat, velit nulla facilisis neque, ac pellentesque enim ligula ut ipsum. Nulla vel sagittis metus. Mauris vulputate, enim eget fringilla laoreet, velit lorem cursus ipsum, at elementum quam purus et lorem.</p>
        <p>Jullam volutpat, nibh ac bibendum ultrices, sem est consectetur elit, ut hendrerit sapien augue nec quam. Nunc felis orci, placerat vitae ornare ut, pellentesque nec nisi. Nulla eleifend eros ut mi adipiscing in suscipit est fermentum. Aliquam gravida tincidunt accumsan. Sed non lectus ut turpis mollis eleifend non vitae velit. Nam lacinia tristique purus, quis euismod velit faucibus malesuada. Integer at justo in enim feugiat fringilla. Etiam vitae quam purus. Aliquam pharetra laoreet faucibus.</p>
      </article>
      <div class="photo photo--team" role="img" aria-label="Photo of two smiling professionals in business attire"></div>
    </div>
  </section>

</div>
</body>
</html>
```